Global Expert Network Firm needs business card design

We need business card design for a new company based in Seoul, South Korea called 'Corwell Insight Partners'. We recruit industry experts covering all countries and connect our client and recruited expert by phone, face-to-face meetings and etc. We are a global expert network firm that is focused on delivering high-quality experts to our clients throughout the world. Our clients include multinational corporations, global consulting firms, private equity firms, venture capital firms, asset management companies.
We have made new logo and please find attachment.(Please use new logo)
Target Market(s)
Global Consulting Firms, Investment Firms, Private Equity Firms, Venture Capital Firms.
Industry/Entity Type
Recruitment
Contact Information for Business Card
We need two Languages (English and Korean Version).
The front is Korean and the back is English version.
[The back] [English]
Company Name: Corwell Insight Partners, Inc.
CEO Name: Daniel Park
Address: #507, Hanbit Bldg, 82 Maebongsan-ro, Dobong-gu, Seoul, 01327, Korea
Tel. +82 2 718 4052
Fax. +82 2 864 1097
Mobile. +82 10 7264 8815
Email: daniel@corwellip.com
Web: www.corwellip.com
[The front] [Korean] => Described in same order as English version.
회사명: 코웰인사이트파트너스(주)
대표이사: 박도현
주소: 서울시 도봉구 매봉산로 82 한빛빌딩 507호
Tel. 02 718 4052
Fax. 02 864 1097
Mobile. 010 7264 8815
Web: www.corwellip.com
Look and feel
Each slider illustrates characteristics of the customer's brand and the style your logo design should communicate.

```html
<!DOCTYPE html>
<html lang="en">
<head>
<meta charset="utf-8">
<title>Corwell Insight Partners – Business Card (English)</title>
<link rel="stylesheet" href="https://fonts.googleapis.com/css2?family=Montserrat:wght@400;600&family=Playfair+Display:wght@700&display=swap">
<style>
  :root {
    --paper: #ffffff;
    --gold: #c9b48b;
    --gold-deep: #a8893f;
    --gold-light: #d9c27a;
    --charcoal: #333333;
    --ink: #3a3a3a;
    --navy: #1e2556;
    --white: #ffffff;
  }
  * { margin: 0; padding: 0; box-sizing: border-box; }
  html, body {
    width: 1200px;
    height: 682px;
    overflow: hidden;
    background: var(--paper);
  }
  .card {
    position: relative;
    width: 1200px;
    height: 682px;
    background: var(--paper);
    overflow: hidden;
  }
  .card__shapes {
    position: absolute;
    inset: 0;
  }
  .shape--gold { fill: url(#goldTone); }
  .shape--charcoal { fill: var(--charcoal); }

  .brand-panel {
    position: absolute;
    top: 0;
    left: 853px;
    width: 347px;
    height: 343px;
    background: var(--navy);
    display: flex;
    align-items: center;
    justify-content: center;
    padding: 0 24px;
  }
  .brand-panel__name {
    font-family: "Montserrat", Arial, sans-serif;
    font-weight: 600;
    font-size: 30px;
    line-height: 1.3;
    letter-spacing: 1px;
    color: var(--white);
    text-align: center;
    text-transform: uppercase;
  }

  .contact {
    position: absolute;
    top: 52px;
    left: 310px;
    width: 550px;
    text-align: center;
  }
  .contact__company {
    font-family: "Playfair Display", Georgia, serif;
    font-weight: 700;
    font-size: 39px;
    line-height: 0.82;
    letter-spacing: -0.3px;
    color: var(--gold);
    text-transform: uppercase;
  }
  .contact__ceo {
    margin-top: 36px;
    font-family: "Montserrat", Arial, sans-serif;
    font-weight: 600;
    font-size: 25px;
    letter-spacing: 1.5px;
    color: var(--gold);
    text-transform: uppercase;
  }
  .contact__details {
    margin-top: 16px;
    list-style: none;
    font-family: "Montserrat", Arial, sans-serif;
    font-weight: 400;
    font-size: 20px;
    line-height: 39.5px;
    letter-spacing: 0.6px;
    color: var(--ink);
  }
</style>
</head>
<body>
  <main class="card">
    <svg class="card__shapes" width="1200" height="682" viewBox="0 0 1200 682">
      <defs>
        <linearGradient id="goldTone" x1="0" y1="0" x2="1" y2="1">
          <stop offset="0" stop-color="#d9c27a"/>
          <stop offset="0.55" stop-color="#b89a4c"/>
          <stop offset="1" stop-color="#a8893f"/>
        </linearGradient>
      </defs>
      <polygon class="shape--gold" points="0,0 383,0 66,317 0,290" role="img" aria-label="Gold glitter texture corner"/>
      <polygon class="shape--charcoal" points="0,288 832,682 0,682"/>
    </svg>

    <aside class="brand-panel">
      <p class="brand-panel__name">Corwell<br>Insight<br>Partners</p>
    </aside>

    <section class="contact">
      <h1 class="contact__company">Company Name:Corwell<br>Insight Partners,Inc.</h1>
      <p class="contact__ceo">CEO Name: Daniel Park</p>
      <ul class="contact__details">
        <li>Address: #507, Hanbit Bldg,</li>
        <li>82 Maebongsan-ro,</li>
        <li>Dobong-gu, Seoul, 01327, Korea</li>
        <li>Tel. +82 2 718 4052</li>
        <li>Fax. +82 2 864 1097</li>
        <li>Mobile. +82 10 7264 8815</li>
        <li>Email: daniel@corwellip.com</li>
        <li>Web: www.corwellip.com</li>
      </ul>
    </section>
  </main>
</body>
</html>
```